Business card design needed

Velvet Twirl-Pop is an online boutique for connoisseurs of unique, hand crafted, vintage and pin-up inspired lingerie, delectable handmade lotions & potions and naughty & nice, seduce me please gifts and ideas.

Inspired by vintage glamour, pin-up and burlesque, the site is dedicated to things that make all women look and feel beautiful…with a touch of mischief.

The design should be clean, uncomplicated, sophisticated and in line with the website - See www.velvettwirlpop.com.au.

Predominantly black, red and grey in colour.

Font used on the website is Honeyscript and Drescher Grotesk Light

Industry/Entity Type

Boutique

Contact Information for Business Card

Velvet Twirl-Pop
Odessa Marlowe - Director
0413 572 064
odessa@velvettwirlpop.com.au

Requirements
Should not have
• No lace, nothing to girly.

```html
<!DOCTYPE html>
<html lang="en">
<head>
<meta charset="utf-8">
<title>Velvet Twirl-Pop — Business Card</title>
<link rel="stylesheet" href="https://fonts.googleapis.com/css2?family=Didact+Gothic&display=swap">
<style>
  :root {
    --page: #ffffff;
    --card-black: #17171a;
    --front-base: #1c1414;
    --front-tone: #3a1a18;
    --brand-red: #b01e17;
    --ink-light: #f2f2f2;
    --text-font: "Didact Gothic", "Century Gothic", sans-serif;
  }
  * { margin: 0; padding: 0; box-sizing: border-box; }
  html, body {
    width: 1200px;
    height: 900px;
    overflow: hidden;
    background: var(--page);
  }
  .sheet {
    position: relative;
    width: 1200px;
    height: 900px;
  }
  .card {
    position: absolute;
    top: 304px;
    width: 506px;
    height: 292px;
    overflow: hidden;
  }
  .card-front {
    left: 86px;
    background: var(--front-base);
  }
  .front-pattern {
    position: absolute;
    inset: 0;
    background:
      radial-gradient(ellipse at 50% 45%, rgba(58, 26, 24, 0.9) 0%, rgba(40, 20, 20, 0.6) 45%, rgba(20, 14, 14, 0) 80%),
      linear-gradient(180deg, var(--front-tone) 0%, var(--front-base) 100%);
    opacity: 0.85;
  }
  .brand-mark {
    position: absolute;
    left: 50%;
    top: 62px;
    width: 90px;
    height: 90px;
    margin-left: -45px;
    border-radius: 50%;
    background: var(--brand-red);
  }
  .brand-name {
    position: absolute;
    left: 0;
    right: 0;
    top: 206px;
    text-align: center;
    font-family: var(--text-font);
    font-size: 31px;
    letter-spacing: 4px;
    color: var(--brand-red);
    white-space: nowrap;
  }
  .card-back {
    left: 608px;
    background: var(--card-black);
    color: var(--ink-light);
    font-family: var(--text-font);
    font-size: 18px;
    text-align: center;
  }
  .holder {
    position: absolute;
    top: 70px;
    left: 0;
    right: 0;
  }
  .holder-block {
    display: inline-block;
    text-align: left;
  }
  .holder-name { display: block; line-height: 22px; }
  .holder-role {
    display: block;
    text-align: right;
    font-style: italic;
    line-height: 20px;
  }
  .web {
    position: absolute;
    top: 146px;
    left: 0;
    right: 0;
    font-style: italic;
    font-size: 19px;
  }
  .contact {
    position: absolute;
    top: 201px;
    left: 0;
    right: 0;
    line-height: 25px;
  }
</style>
</head>
<body>
  <main class="sheet">
    <section class="card card-front">
      <div class="front-pattern" role="img" aria-label="Dark red damask pattern with large faint swirling decoration"></div>
      <div class="brand-mark"></div>
      <div class="brand-name">VELVET TWIRL-POP</div>
    </section>

    <section class="card card-back">
      <div class="holder">
        <div class="holder-block">
          <span class="holder-name">Velvet Twirl-Pop Odessa Marlowe</span>
          <span class="holder-role">Director</span>
        </div>
      </div>
      <p class="web">www.velvettwirlpop.com.au</p>
      <p class="contact">0413 572 064<br>odessa@velvettwirlpop.com.au</p>
    </section>
  </main>
</body>
</html>
```